Divorce Lawyer print and ebook cover (Planting gardens after every storm )

I need a front and back cover for my divorce and family law book. I already have a photo and title. The back cover photo is not necessary but can be interesting the Front-main cover is a must

Target Market(s)

Prospective client

Colors

Designer to choose colors to be used in the design.

Requirements
Must have
• Front photo by viewable.

```html
<!DOCTYPE html>
<html lang="en">
<head>
<meta charset="utf-8">
<title>Planting gardens after every storm – cover spread</title>
<link rel="stylesheet" href="https://fonts.googleapis.com/css2?family=Roboto+Slab:wght@400;600;700&family=Fredoka:wght@600&family=Open+Sans:wght@400;600&display=swap">
<style>
  :root {
    --teal: #17a39e;
    --teal-mid: #128a88;
    --teal-deep: #0e5f66;
    --teal-pale: #6fc9c3;
    --gold: #f2dc6b;
    --white: #ffffff;
    --label: #6b6b6b;
    --paper: #ffffff;
  }
  * { margin: 0; padding: 0; box-sizing: border-box; }
  html, body { width: 1200px; height: 854px; overflow: hidden; background: var(--paper); }
  .spread { position: relative; width: 1200px; height: 854px; }
  .side-label {
    position: absolute; top: 100px; width: 432px; text-align: center;
    font: 400 26px "Open Sans", sans-serif; color: var(--label);
  }
  .side-label.front { left: 128px; }
  .side-label.back { left: 644px; }
  .cover { position: absolute; top: 170px; width: 432px; height: 613px; overflow: hidden; }
  .cover.front { left: 128px; }
  .cover.back { left: 644px; }
  .cover svg.art { position: absolute; inset: 0; }
  .title { position: absolute; right: 46px; top: 40px; text-align: right; }
  .title .line-1 { font: 700 27px "Roboto Slab", serif; color: var(--white); letter-spacing: .5px; }
  .title .line-2 { font: italic 400 18px "Roboto Slab", serif; color: var(--white); margin-right: 120px; line-height: 1.1; }
  .title .line-3 { font: 600 34px "Fredoka", sans-serif; color: var(--gold); line-height: 1.05; }
  .author {
    position: absolute; right: 36px; top: 536px;
    font: 400 24px "Roboto Slab", serif; color: var(--teal);
  }
  .quotes { position: absolute; left: 92px; top: 287px; width: 90px; color: var(--white);
    font: 600 7.6px/10.4px "Roboto Slab", serif; }
  .quotes p + p { margin-top: 18px; }
  .photo-box { position: absolute; left: 184px; top: 286px; width: 230px; height: 182px; border-radius: 7px; overflow: hidden; }
  .footer { position: absolute; left: 30px; top: 566px; display: flex; align-items: center; gap: 10px;
    font: 400 7.5px "Open Sans", sans-serif; color: var(--white); }
  .brand { display: flex; align-items: center; gap: 4px; font: 600 8px "Open Sans", sans-serif; }
  .brand .mark { width: 14px; height: 14px; background: var(--white); border-radius: 2px; }
  .contact { display: flex; align-items: center; gap: 3px; }
</style>
</head>
<body>
<div class="spread">
  <div class="side-label front">Front</div>
  <div class="side-label back">Back</div>

  <section class="cover front">
    <svg class="art" width="432" height="613" viewBox="0 0 432 613">
      <defs>
        <linearGradient id="scene" x1="0" y1="0" x2="1" y2="0.3">
          <stop offset="0" stop-color="#5f6f7a"/>
          <stop offset="0.4" stop-color="#b9c4c6"/>
          <stop offset="0.75" stop-color="#d8d48a"/>
          <stop offset="1" stop-color="#b7a440"/>
        </linearGradient>
        <linearGradient id="ground" x1="0" y1="0" x2="0" y2="1">
          <stop offset="0" stop-color="#000" stop-opacity="0"/>
          <stop offset="1" stop-color="#1d2a35" stop-opacity="0.85"/>
        </linearGradient>
      </defs>
      <g role="img" aria-label="Photo: a man in a suit standing at a fork in a misty forest road, with signposts pointing to an old and a new life">
        <rect width="432" height="566" fill="url(#scene)"/>
        <rect y="260" width="432" height="306" fill="url(#ground)"/>
      </g>
      <path d="M0 0H432V112C380 140 320 175 285 195C262 209 245 211 220 200L0 86Z" fill="var(--teal-pale)"/>
      <path d="M0 0H432V106C378 134 320 168 282 188C260 200 244 202 222 192L0 74Z" fill="var(--teal-mid)"/>
      <g stroke="var(--teal-pale)" stroke-width="1.4" opacity=".6">
        <line x1="370" y1="0" x2="250" y2="160"/><line x1="388" y1="0" x2="262" y2="168"/>
        <line x1="406" y1="0" x2="274" y2="176"/><line x1="424" y1="0" x2="286" y2="184"/>
      </g>
      <rect y="566" width="432" height="47" fill="var(--teal)"/>
    </svg>
    <div class="title">
      <div class="line-1">PLANTING GARDENS</div>
      <div class="line-2">after every</div>
      <div class="line-3">STORM</div>
    </div>
    <div class="author">Author’s name</div>
  </section>

  <section class="cover back">
    <svg class="art" width="432" height="613" viewBox="0 0 432 613">
      <rect width="432" height="613" fill="var(--teal)"/>
      <path d="M0 110L170 210C195 224 225 226 250 214L432 110V0H0Z" fill="var(--teal-deep)"/>
      <path d="M0 110L170 210C195 224 225 226 250 214L432 110" fill="none" stroke="var(--teal-pale)" stroke-width="6"/>
      <path d="M120 0H432V82L350 118C310 136 280 118 250 96Z" fill="var(--teal-mid)"/>
      <g stroke="var(--teal-pale)" stroke-width="1.3" opacity=".6">
        <line x1="0" y1="10" x2="220" y2="150"/><line x1="0" y1="24" x2="225" y2="168"/>
        <line x1="0" y1="38" x2="230" y2="186"/><line x1="0" y1="52" x2="235" y2="204"/>
      </g>
      <path d="M0 225L0 495L50 420C82 372 85 330 55 290Z" fill="var(--teal-deep)"/>
      <path d="M0 225L55 290C85 330 82 372 50 420L0 495" fill="none" stroke="var(--teal-pale)" stroke-width="3"/>
      <path d="M0 330C20 350 22 380 0 410Z" fill="var(--teal)"/>
      <rect x="426" y="0" width="6" height="613" fill="var(--teal-mid)"/>
    </svg>
    <div class="quotes">
      <p>“Lorem ipsum dolor sit amet, consectetur adipiscing elit, sed do eiusmod tempor incididunt ut labore et dolore magna aliqua. Ut enim ad minim veniam”</p>
      <p>“Lorem ipsum dolor sit amet, consectetur adipiscing elit”</p>
    </div>
    <div class="photo-box" role="img" aria-label="Photo: a small child in a knitted hat sitting on a playground swing, held by two adults" style="background: linear-gradient(135deg, #9a9489, #7d7466 55%, #5e574c);"></div>
    <div class="footer">
      <div class="brand"><span class="mark"></span>Harbor Law</div>
      <div class="contact">
        <svg width="9" height="9" viewBox="0 0 10 10"><circle cx="5" cy="5" r="4.4" fill="none" stroke="#fff" stroke-width=".8"/><path d="M3.3 3c.3 1.8 1.5 3.2 3.4 3.8l.5-.8-.9-.5-.4.4C5 5.5 4.5 5 4.3 4.2l.4-.4-.5-.9Z" fill="#fff"/></svg>
        001 555 0142
      </div>
      <div class="contact">
        <svg width="9" height="9" viewBox="0 0 10 10"><circle cx="5" cy="5" r="4.4" fill="none" stroke="#fff" stroke-width=".8"/><rect x="2.8" y="3.5" width="4.4" height="3" fill="none" stroke="#fff" stroke-width=".6"/><path d="M2.8 3.5 5 5.2 7.2 3.5" fill="none" stroke="#fff" stroke-width=".6"/></svg>
        Your e-mail here
      </div>
    </div>
  </section>
</div>
</body>
</html>
```